Wordpress Design Project - Australian Solar Company wants to start FRESH!

About us

Bright Meadow are a renewable energy company based in Perth Australia, but we also have offices all over Asia. We specialise in offering renewable energy solutions (Solar PV Systems and LED Lighting) to residential and commercial customers.

Our current website: www.brightmeadowenergy.com.au

Our needs

This will be a replacement website as we are not happy with our current layout. We have an Australian company doing our SEO and they have recommended a new layout which we wish to go with.

We really want a professional and easy to navigate website that will assist in bringing in more enquiries and phone calls.

Content

We have all the content and will get the design winner to add this after we have chosen the design we like.
It is important that the call to actions are presented well and are visible these are things like the free quote form and our phone number.

The layout as we have advised has been based on SEO research so we wish it to be exactly the same unless otherwise stated.

Call to action

Our main objective of the new website is for people to come to the home page and see us as a professional and reliable company to deal with and enquire further.

We really want as many people as we can to convert to a lead. We want every person that comes to the website to enquire online or call us. We feel it is important to have a contact us/quote form on every page of the website.

Functional requirements

We have a chatterbook and vidstream account so links to these would be needed

Design assets

The logo needs to be displayed as shown in the website layout brief

Colours – we would like fresh, subdued colours that are professional and appealing to the eye. We ask that you do not take the colours from the logo.

Current website dislikes – the things we currently dislike about our current website is that it is hard to find information and there is no clear call to action. The colours are really unappealing as well as it looks cheap not professional.
The graphics that we require for the slider on the home page will have to be given after the winner is chosen but we want there to be three sliders on rotation

- Credibility builder (employee infront of solar panel) that encourages we use all our own employees not subcontractors
- Residential Slider – picture of a couple and solar panel system with a testimonial
- Commercial slider – picture of commercial system with “find out how you can install solar for free* at your business”

Design ideas

The website needs to be mobile friendly as well
It is going to be a total rebuild from the current website as our current website really isn’t working for us.

Target Market(s)

Target Audience

Our target audience are both residential and commercial clients
Residential – we want to attract home owners that are interested in reducing their electricity bill and helping the environment. Generally these people are between the ages of 28-50+ both male and female.

Commercial – We want to appeal to key decision makers within the commercial sphere. For example – CEOs, Company Directors, Operation managers and business owners of any industry. These people will be interested in reducing their electricity bills and creating a clean green image for their business.
Our target audience will generally come to our website to get information and enquire for a quote/ product information.

Industry/Entity Type

Residential

Requirements
Must have
• MUST BE LAID OUT LIKE THIS:

http://www.docuvault.com/doc/849302715/Website-Layout

Must have Enquire Now forms on every page that read:

Name
Phone Number
How did you hear about us
Message

```html
<!DOCTYPE html>
<html lang="en">
<head>
<meta charset="utf-8">
<title>Bright Meadow — Home</title>
<link href="https://fonts.googleapis.com/css2?family=Open+Sans:wght@400;600&family=Noto+Serif&display=swap" rel="stylesheet">
<style>
:root{
  --green:#1f8f3a;
  --green-dark:#177a2f;
  --green-light:#7fbf6a;
  --band-top:#2e9a3e;
  --orange:#f3a712;
  --orange-border:#efc05a;
  --nav:#3b3b3b;
  --text:#333;
  --muted:#444;
  --page:#f1f1f1;
  --footer:#333;
  --white:#fff;
}
*{box-sizing:border-box;margin:0;padding:0}
html,body{width:947px;height:1200px;overflow:hidden}
body{position:relative;background:var(--page);font-family:"Open Sans",Arial,sans-serif;color:var(--text)}
.abs{position:absolute}
.top-band{left:0;top:0;width:947px;height:310px;background:linear-gradient(#2f9a3f 0%,#4fae55 35%,#7cc06a 55%,#2f9a3c 80%,#1e8c33 100%)}
.social{top:7px;left:782px;display:flex;gap:4px}
.social span{width:18px;height:18px;background:#2a2a2a;border-radius:2px;display:block}
.header{left:94px;top:33px;width:758px;height:82px;background:var(--white);border:1px solid var(--green)}
.brand{left:12px;top:30px;font-size:20px;font-weight:600;color:var(--green);display:flex;align-items:center;gap:8px}
.brand i{width:14px;height:14px;border-radius:50%;background:var(--orange);display:block}
.call{right:6px;top:12px;font-family:"Noto Serif",Georgia,serif;font-size:12px;color:#222;display:flex;align-items:baseline;gap:4px}
.call b{font-weight:400;font-size:19px;color:#333}
.call b em{font-style:normal;color:var(--orange)}
.nav{left:244px;top:44px;width:505px;height:26px;background:linear-gradient(#4a4a4a,#2e2e2e);display:flex;justify-content:space-around;align-items:center;border-bottom:2px solid #777}
.nav a{color:#fff;font-size:10px;font-weight:600;text-decoration:none}
.slider{left:94px;top:130px;width:758px;height:324px;background:var(--white);padding:4px;box-shadow:0 12px 10px -8px rgba(0,0,0,.5)}
.slide{width:100%;height:100%;background:linear-gradient(100deg,#2b55b8 0%,#4f7fd6 30%,#9cc3ea 48%,#b9d9f0 58%,#7fb24a 75%,#5f9a2e 100%)}
.quote{left:608px;top:170px;width:204px;height:233px;background:rgba(70,70,70,.72);border-radius:3px;color:#fff}
.quote h2{font-size:14px;font-weight:600;text-align:center;margin-top:15px}
.quote .row{position:absolute;left:16px;font-size:10px;font-weight:600}
.quote .field{position:absolute;left:66px;width:122px;height:18px;background:#fff;border:1px solid #ccc;font-size:8px;font-style:italic;color:#888;padding:3px 7px}
.quote .submit{position:absolute;left:116px;top:193px;width:72px;height:21px;background:linear-gradient(#ffc02a,#f09a00);color:#333;font-size:9px;font-weight:600;text-align:center;line-height:21px;border-radius:2px}
.dots{left:450px;top:463px;display:flex;gap:6px}
.dots span{width:8px;height:8px;border-radius:50%;background:#c8c8c8}
.dots span.on{background:var(--green)}
.service{width:174px;text-align:center}
.service h3{height:38px;font-size:13.5px;font-weight:400;color:#222;line-height:19px;display:flex;align-items:center;justify-content:center}
.service .thumb{margin-top:0;height:106px;border:3px solid #fff;box-shadow:0 0 3px rgba(0,0,0,.3)}
.service p{font-size:9.5px;line-height:14px;margin-top:22px;color:var(--muted)}
.btn{display:inline-block;background:linear-gradient(#2aa34a,#17802f);color:#fff;font-size:9.5px;padding:3px 7px;border-radius:1px}
.service .btn{margin-top:12px}
.panel{top:782px;width:365px;height:205px;background:#fff;border:1px solid var(--orange-border)}
.panel h2{position:absolute;font-size:13.5px;font-weight:400;color:#222}
.panel p{position:absolute;font-size:9.5px;line-height:16px;color:var(--muted)}
.link{position:absolute;font-size:10px;font-style:italic;color:var(--green)}
.arrows{right:18px;top:15px;display:flex;gap:3px}
.arrows span{width:11px;height:11px;border-radius:50%;background:var(--orange)}
.vid{position:absolute;left:16px;width:80px;height:55px;display:flex;align-items:center;justify-content:center}
.card{top:1019px;width:174px;height:67px;background:linear-gradient(#fff,#ececec);border:1px solid #c9c9c9;display:flex;align-items:center;gap:14px;padding-left:14px}
.card svg{flex:none}
.card .label{font-size:13.5px;line-height:18px;color:#333}
.card .label span{color:var(--green);display:block}
.footer{left:0;top:1120px;width:947px;height:80px;background:var(--footer);color:#fff;text-align:center}
.footer nav{margin-top:25px;font-size:11px}
.footer nav a{color:#fff;text-decoration:none;margin:0 7px}
.footer small{display:block;margin-top:17px;font-size:9px;color:#ccc}
</style>
</head>
<body>
<div class="abs top-band"></div>
<div class="abs social"><span></span><span></span><span></span></div>

<header class="abs header">
  <div class="abs brand"><i></i>Bright Meadow</div>
  <div class="abs call">
    <svg width="14" height="14" viewBox="0 0 24 24"><path fill="#222" d="M6.6 10.8a15 15 0 0 0 6.6 6.6l2.2-2.2c.3-.3.7-.4 1-.2 1.1.4 2.3.6 3.6.6.6 0 1 .4 1 1V20c0 .6-.4 1-1 1A17 17 0 0 1 3 4c0-.6.4-1 1-1h3.5c.6 0 1 .4 1 1 0 1.3.2 2.5.6 3.6.1.3 0 .7-.2 1z"/></svg>
    Call Us <b>-1300.574.<em>296</em></b>
  </div>
  <nav class="abs nav">
    <a>Home</a><a>About</a><a>Products</a><a>Services</a><a>Projects</a><a>Media</a><a>Information</a><a>Enquiry</a><a>Contacts</a>
  </nav>
</header>

<section class="abs slider">
  <div class="slide" role="img" aria-label="Rows of blue solar panels on green grass under a bright blue sky"></div>
</section>
<form class="abs quote">
  <h2>Quote Online</h2>
  <span class="row" style="top:66px">Name</span><span class="field" style="top:62px">Enter name</span>
  <span class="row" style="top:94px">Email</span><span class="field" style="top:90px">Enter your Email..</span>
  <span class="row" style="top:122px">Phone</span><span class="field" style="top:118px">Phone no..</span>
  <span class="row" style="top:150px">Message</span><span class="field" style="top:146px;height:48px">Message...</span>
  <span class="submit">SUBMIT</span>
</form>
<div class="abs dots"><span class="on"></span><span></span><span></span><span></span></div>

<article class="abs service" style="left:102px;top:504px">
  <h3>Perth Residential Solar Power</h3>
  <div class="thumb" style="background:linear-gradient(#6fa7e0,#9cc6ef 40%,#c06a3c 70%,#e8e4dc)" role="img" aria-label="House roof fitted with solar panels"></div>
  <p>Lorem Ipsum is simply dummy text of the printing &amp; typsetting industry.</p>
  <span class="btn">Read More</span>
</article>
<article class="abs service" style="left:292px;top:504px">
  <h3>Perth Commercial Solar Power</h3>
  <div class="thumb" style="background:linear-gradient(90deg,#7aa5d8,#3a3f55 45%,#5a86c8)" role="img" aria-label="Engineer in hard hat beside commercial solar array"></div>
  <p>Lorem Ipsum is simply dummy text of the printing &amp; typsetting industry.</p>
  <span class="btn">Read More</span>
</article>
<article class="abs service" style="left:481px;top:504px">
  <h3>Perth Air Conditioning WA</h3>
  <div class="thumb" style="background:linear-gradient(90deg,#8a8f98,#b8bcc2 45%,#2e3444)" role="img" aria-label="Technician servicing an air conditioning unit"></div>
  <p>Lorem Ipsum is simply dummy text of the printing &amp; typsetting industry.</p>
  <span class="btn">Read More</span>
</article>
<article class="abs service" style="left:670px;top:504px">
  <h3>Perth LED Lighting</h3>
  <div class="thumb" style="background:linear-gradient(#d83a2a,#e8a22a 35%,#2f9a2a 70%,#0f3a10)" role="img" aria-label="Close-up of coloured LED bulbs"></div>
  <p>Lorem Ipsum is simply dummy text of the printing &amp; typsetting industry.</p>
  <span class="btn">Read More</span>
</article>

<section class="abs panel" style="left:102px">
  <div class="abs" style="left:12px;top:14px;width:152px;height:94px;border:2px solid #fff;box-shadow:0 0 3px rgba(0,0,0,.3);background:linear-gradient(90deg,#2d4f9c,#5c7fc4 60%,#3a5a9e)" role="img" aria-label="Engineer holding plans in front of solar panels"></div>
  <h2 style="left:177px;top:14px">Welcome to Bright Meadow</h2>
  <p style="left:180px;top:46px;width:170px">Lorem ipsum dolor sit amet, conse ur adipisicing elit, sed do eiusmod tempor incididunt ut labore et dolr magna aliqua.</p>
  <p style="left:14px;top:124px;width:340px">nisi ut aliquip ex ea commodo consequat. Duis aute irure dolor in Ut enim ad minim veniam, quis nostrud exercitation ullamco laboris.</p>
  <span class="btn abs" style="right:16px;top:168px">Read More</span>
</section>

<section class="abs panel" style="left:481px">
  <h2 style="left:15px;top:14px">Testimonials</h2>
  <div class="abs arrows"><span></span><span></span></div>
  <div class="vid" style="top:48px;background:linear-gradient(#7fa8d8,#3a5f9e)" role="img" aria-label="Video still of installers on a roof">
    <svg width="24" height="24" viewBox="0 0 24 24"><circle cx="12" cy="12" r="12" fill="rgba(40,40,40,.75)"/><path d="M9 7l8 5-8 5z" fill="#fff"/></svg></div>
  <span class="link" style="left:114px;top:50px">Click here to watch the video!</span>
  <p style="left:114px;top:72px;width:240px">nisi ut aliquip ex ea commodo consequat. Duis aute irure dolor in nostrud ullamco laboris.</p>
  <div class="vid" style="top:124px;background:linear-gradient(90deg,#3a3028,#c08a50,#6a4a30)" role="img" aria-label="Video still of hands holding a light bulb">
    <svg width="24" height="24" viewBox="0 0 24 24"><circle cx="12" cy="12" r="12" fill="rgba(40,40,40,.75)"/><path d="M9 7l8 5-8 5z" fill="#fff"/></svg></div>
  <span class="link" style="left:116px;top:130px">Click here to watch the video!</span>
  <p style="left:116px;top:152px;width:240px">nisi ut aliquip ex ea commodo consequat. Duis aute irure dolor in nostrud ullamco laboris.</p>
</section>

<a class="abs card" style="left:102px">
  <svg width="40" height="40" viewBox="0 0 40 40"><circle cx="20" cy="20" r="14" fill="none" stroke="#f5a80f" stroke-width="7" stroke-dasharray="5.5 5.5"/><circle cx="20" cy="20" r="11" fill="#f5a80f"/><circle cx="20" cy="20" r="5" fill="#f4f4f4"/></svg>
  <div class="label"><span>Primary Prod.</span>/ Services</div>
</a>
<a class="abs card" style="left:292px">
  <svg width="48" height="40" viewBox="0 0 48 40"><circle cx="17" cy="11" r="7" fill="#f5a80f"/><path d="M4 36c0-10 6-15 13-15s13 5 13 15z" fill="#f5a80f"/><circle cx="33" cy="15" r="6" fill="#f5a80f"/><path d="M26 36c1-8 4-12 8-12s10 4 10 12z" fill="#f5a80f"/></svg>
  <div class="label"><span>Memberships</span>dolor sit</div>
</a>
<a class="abs card" style="left:482px">
  <svg width="40" height="40" viewBox="0 0 40 40"><rect x="4" y="8" width="26" height="28" fill="none" stroke="#f5a80f" stroke-width="3"/><path d="M14 26l3-7 15-15 4 4-15 15z" fill="#f5a80f"/></svg>
  <div class="label"><span>Request</span>Quotation</div>
</a>
<a class="abs card" style="left:671px">
  <svg width="52" height="40" viewBox="0 0 52 40"><rect x="4" y="4" width="18" height="32" rx="3" fill="none" stroke="#f5a80f" stroke-width="3"/><circle cx="30" cy="14" r="5" fill="#f5a80f"/><path d="M22 30c0-7 4-10 8-10s8 3 8 10z" fill="#f5a80f"/><circle cx="43" cy="12" r="5" fill="#f5a80f"/><path d="M36 24c1-5 4-7 7-7s7 2 7 7z" fill="#f5a80f"/></svg>
  <div class="label"><span>Contact</span>Information</div>
</a>

<footer class="abs footer">
  <nav><a>Home</a>|<a>About</a>|<a>Products</a>|<a>Services</a>|<a>Projects</a>|<a>Media</a>|<a>Information</a>|<a>Enquiry</a>|<a>Contacts</a></nav>
  <small>Copyright.2013. Bright Meadow. All Right Reserved</small>
</footer>
</body>
</html>
```